Falverino’s Artisan Pizzeria Menu Contest

I’m looking for a menu design for a new pizzeria - it’s farm to table type of restaurant - more upscale than a typical pizzeria - white washed wood interior with some industrial accents - I am looking for a creative menu layout using the attached sample menu items -
Falverino’s is an artisanal pizzeria with an atmosphere that will make you feel at home for any situation, first date, anniversary, business lunch, boys night out or girls night out with a menu inspired by the idea of a simple honest cooking paired with fresh – quality ingredients. Full service dining experience that is still casual but dedicated to extraordinary hospitality.
While developing the menu we have created a network of amazing farms and purveyors to supply our restaurant with fresh milled 100% California flour for our hand crafted dough, as well as sustainably farmed organic produce, meats and cheeses.
The menu includes classics like the Margherita pizza to daily seasonal specials, fresh salads to rustic small plates including moms meatball recipe to a fresh local burrata with handmade bread. Each dish reflects our passion for sourcing the freshest quality local ingredients.
To compliment the menu, Falverino’s serves an extensive wine list with selections focusing on Italian varietals. The cocktail program has been carefully crafted to offer something to entice ever palate and the beer list has unique selections of the world’s finest brewers.
Target Market(s)
25-45 year old men and women
Industry/Entity Type
American Restaurant
Requirements
Must have
- professional tone
Nice to have
- a balance of elegance and industrial (rustic)
Should not have
- photos or playful graphics etc..

```html
<!DOCTYPE html>
<html lang="en">
<head>
<meta charset="utf-8">
<title>Falverino’s Artisan Pizzeria Menu</title>
<link href="https://fonts.googleapis.com/css2?family=Josefin+Sans:wght@400;600&family=Didact+Gothic&family=Open+Sans:ital,wght@0,600;1,400&display=swap" rel="stylesheet">
<style>
:root{
  --ink:#161616;
  --paper:#fbfbfa;
  --page:#ffffff;
  --white:#ffffff;
}
*{margin:0;padding:0;box-sizing:border-box}
html,body{width:1200px;height:1000px;overflow:hidden;background:var(--page)}
.canvas{position:relative;width:1200px;height:1000px}
.menu-border{position:absolute;left:20px;top:100px;width:1160px;height:775px;background:var(--ink)}
.menu-sheet{position:absolute;left:55px;top:130px;width:1090px;height:710px;background:var(--paper)}
.frame{position:absolute;left:0;top:0}
.brand{position:absolute;left:500px;top:150px;width:206px;text-align:center;font-family:"Josefin Sans",sans-serif;font-weight:600;font-size:30px;color:var(--ink);letter-spacing:1px}
.section-bar{position:absolute;height:22px;background:var(--ink);color:var(--white);font-family:"Josefin Sans",sans-serif;font-size:17px;line-height:24px;padding-left:4px;text-transform:uppercase}
.item{position:absolute;width:270px}
.item-head{display:flex;justify-content:space-between;font-family:"Didact Gothic",sans-serif;font-size:13px;line-height:16px;color:var(--ink)}
.price{font-family:"Open Sans",sans-serif;font-weight:600;font-size:13px}
.item-desc{font-family:"Open Sans",sans-serif;font-style:italic;font-size:9.5px;line-height:12.5px;color:var(--ink);width:215px}
.boxed{position:absolute;border:2px solid var(--ink)}
.box-title{position:absolute;left:50%;transform:translateX(-50%);top:-12px;background:var(--paper);padding:0 6px;font-family:"Josefin Sans",sans-serif;font-size:17px;color:var(--ink);white-space:nowrap}
.soup-line{position:absolute;left:0;right:0;top:17px;text-align:center;font-family:"Didact Gothic",sans-serif;font-size:13px;color:var(--ink)}
.crust{position:absolute;left:0;right:0;text-align:center;color:var(--ink)}
.crust-name{font-family:"Didact Gothic",sans-serif;font-size:13px;line-height:16px}
.crust-desc{font-family:"Open Sans",sans-serif;font-style:italic;font-size:9.5px;line-height:13px}
.dips{position:absolute;left:826px;top:680px;width:273px;height:126px;background:var(--ink);padding:4px}
.dips-inner{width:100%;height:100%;border:1.5px solid var(--white);position:relative;color:var(--white)}
.dips-title{text-align:center;font-family:"Josefin Sans",sans-serif;font-size:17px;padding-top:8px}
.dip{position:absolute;left:17px;right:17px;display:flex;justify-content:space-between;font-family:"Didact Gothic",sans-serif;font-size:13px}
.dip .price{color:var(--white)}
</style>
</head>
<body>
<div class="canvas">
  <div class="menu-border"></div>
  <div class="menu-sheet"></div>
  <svg class="frame" width="1200" height="1000" aria-hidden="true">
    <path d="M498 168 V128 Q603 116 708 128 V168 H1133 V828 H68 V168 Z" fill="none" stroke="#161616" stroke-width="3"/>
    <path d="M504 166 V133 Q603 122 702 133 V166" fill="#fbfbfa" stroke="none"/>
  </svg>
  <div class="brand">Falverino’s</div>

  <!-- Left column -->
  <div class="section-bar" style="left:100px;top:253px;width:273px">Appetizer</div>
  <div class="item" style="left:103px;top:291px"><div class="item-head"><span>Brussels</span><span class="price">$10.00</span></div><div class="item-desc">Pan seared brussel sprouts with a drizzle of balsamic reduction and parm and bread crumbs Meatballs</div></div>
  <div class="item" style="left:103px;top:350px"><div class="item-head"><span>Meatballs</span><span class="price">$13.00</span></div><div class="item-desc">Moms meatballs handmade secret recipe for over 75 years</div></div>
  <div class="item" style="left:103px;top:396px"><div class="item-head"><span>Mussels</span><span class="price">$15.00</span></div><div class="item-desc">New Zealand Mussels in a tomato broth</div></div>
  <div class="item" style="left:103px;top:432px"><div class="item-head"><span>Romanesco</span><span class="price">$11.00</span></div><div class="item-desc" style="width:260px">Flash fried romanesco served atop a spicy aioli</div></div>
  <div class="item" style="left:103px;top:467px"><div class="item-head"><span>Chicken Wings</span><span class="price">$10.00</span></div><div class="item-desc">Italian fried chicken wings with a kick</div></div>
  <div class="item" style="left:103px;top:500px"><div class="item-head"><span>Burrata</span><span class="price">$13.00</span></div><div class="item-desc">Local burrata served with apples grapes and fresh made bread</div></div>

  <div class="section-bar" style="left:100px;top:558px;width:273px">Salads</div>
  <div class="item" style="left:103px;top:593px"><div class="item-head"><span>Chopped Salad</span><span class="price">$13.00</span></div><div class="item-desc" style="width:260px">Lettuce mix with tomato, onions, peppers, pepperoni, chick peas, fresh mozz, italian herb ving</div></div>
  <div class="item" style="left:103px;top:642px"><div class="item-head"><span>Caesar Salad</span><span class="price">$11.00</span></div><div class="item-desc">Traditional caesar salad rich and creamy extra shaved parmesan</div></div>
  <div class="item" style="left:103px;top:688px"><div class="item-head"><span>Farm Salad</span><span class="price">$15.00</span></div><div class="item-desc">Seasonal farmers market salad</div></div>
  <div class="item" style="left:103px;top:721px"><div class="item-head"><span>Grilled Little Gem</span><span class="price">$11.00</span></div><div class="item-desc">Grilled little gems with bacon, tomato, red onions and blue cheese dressing</div></div>
  <div class="item" style="left:103px;top:769px"><div class="item-head"><span>Spinach and Arugula Salad</span><span class="price">$12.00</span></div><div class="item-desc">Spinach and argula, red pepperstossed in a lemon ving and housemade croutons</div></div>

  <!-- Middle column -->
  <div class="section-bar" style="left:463px;top:253px;width:273px">Sandwiches</div>
  <div class="item" style="left:466px;top:291px"><div class="item-head"><span>Italian Sub</span><span class="price">$13.00</span></div><div class="item-desc">Prociutto, salumi, turkey, provolone, lettuce, tomato and herb aioli with spicy gardenia</div></div>
  <div class="item" style="left:466px;top:335px"><div class="item-head"><span>Turkey Sandwich</span><span class="price">$12.00</span></div><div class="item-desc">housemade bread - turkey, cheddar cheese, butter lettuce, tomato and mustard aioli</div></div>
  <div class="item" style="left:466px;top:381px"><div class="item-head"><span>Meatball Sub</span><span class="price">$13.00</span></div><div class="item-desc">Moms meatballs melted provolone on a housemade roll</div></div>
  <div class="item" style="left:466px;top:427px"><div class="item-head"><span>Verdant Burger</span><span class="price">$14.00</span></div><div class="item-desc">Housemade bun - arugula , tomato, onion and a sundried tomato spread</div></div>
  <div class="item" style="left:466px;top:473px"><div class="item-head"><span>Chicken Burger</span><span class="price">$13.00</span></div><div class="item-desc">Fried chicken or chicken breast, provolone, argula, tomato, served with a spicy aioli</div></div>

  <div class="boxed" style="left:465px;top:533px;width:271px;height:45px">
    <div class="box-title">DAILY SOUP</div>
    <div class="soup-line" style="top:16px">Example Tomato bisque&nbsp; <span class="price">$8.00</span></div>
  </div>

  <div class="section-bar" style="left:463px;top:592px;width:273px">Pizzas</div>
  <div class="item" style="left:466px;top:627px"><div class="item-head"><span>Margherita</span><span class="price">$14.00</span></div><div class="item-desc">Classic Margherita pizza - Fresh Mozz Tomato Sauce and Basil</div></div>
  <div class="item" style="left:466px;top:672px"><div class="item-head"><span>Organic Sausage</span><span class="price">$16.00</span></div><div class="item-desc">Organic Sausage Housemade Red Sauce Mozz hint of fennel</div></div>
  <div class="item" style="left:466px;top:720px"><div class="item-head"><span>Pepperoni</span><span class="price">$16.00</span></div><div class="item-desc">Hollis Pepperoni - Housemade Red Sauce Chile flakes and Mozz</div></div>
  <div class="item" style="left:466px;top:767px"><div class="item-head"><span>Salumi and Burrata</span><span class="price">$17.00</span></div><div class="item-desc">Salumi dried Red Sauce finished with whipped burrata</div></div>

  <!-- Right column -->
  <div class="item" style="left:828px;top:250px;width:266px"><div class="item-head"><span>Mushroom</span><span class="price">$15.00</span></div><div class="item-desc">Shaved mushrooms with a Parmesan cream and melted onions</div></div>
  <div class="item" style="left:828px;top:296px;width:266px"><div class="item-head"><span>Prosciutto and Egg</span><span class="price">$16.00</span></div><div class="item-desc" style="width:180px">Parma Prosciutto Parmesan cream with Dalsberg and gruyere finished with an organic egg</div></div>
  <div class="item" style="left:828px;top:355px;width:266px"><div class="item-head"><span>Quattro Formaggi</span><span class="price">$15.00</span></div><div class="item-desc" style="width:170px">Four cheese combination - mozz - fontina - parm cream and gruyere chile flakes and oregano</div></div>
  <div class="item" style="left:828px;top:416px;width:266px"><div class="item-head"><span>Farmers Pizza</span><span class="price">$17.00</span></div><div class="item-desc" style="width:190px">Seasonal vegatables cream sauce and a variety of cheese</div></div>
  <div class="item" style="left:828px;top:465px;width:266px"><div class="item-head"><span>Keto Friendly</span><span class="price">$17.00</span></div><div class="item-desc" style="width:180px">Cauliflower crust, spinach and kale, parm cream sauce</div></div>
  <div class="item" style="left:828px;top:518px;width:266px"><div class="item-head"><span>Daily Special</span><span class="price">$17.00</span></div></div>

  <div class="boxed" style="left:827px;top:552px;width:271px;height:113px">
    <div class="box-title">CRUSTS</div>
    <div class="crust" style="top:10px"><div class="crust-name">Traditional</div><div class="crust-desc">Orginal crust you can't miss</div></div>
    <div class="crust" style="top:48px"><div class="crust-name">Gluten Free <span class="price">$3.00</span></div><div class="crust-desc">Best gluten friendly crust on the west coast</div></div>
    <div class="crust" style="top:81px"><div class="crust-name">Cauliflower <span class="price">$3.00</span></div><div class="crust-desc">Vegans have needs</div></div>
  </div>

  <div class="dips">
    <div class="dips-inner">
      <div class="dips-title">DIPS</div>
      <div class="dip" style="top:29px"><span>Ranch</span><span class="price">$1.00</span></div>
      <div class="dip" style="top:51px"><span>Tomato Sauce</span><span class="price">$1.00</span></div>
      <div class="dip" style="top:73px"><span>Spicy Dip</span><span class="price">$1.00</span></div>
      <div class="dip" style="top:94px"><span>Blue Cheese</span><span class="price">$1.00</span></div>
    </div>
  </div>
</div>
</body>
</html>
```